Physiotherapy business needs patient information graphic redesign

We have existing graphics that we need redesigned to add some artistic flare. The images must remain professional and suitable for a healthcare setting but some artistic flare is need to add interest to the graphics so that patients are able to engage more easily with the info sheet. Graphics include "INS", "graded activity", "pacing I", "pacing II" and "sleep"

Target Market(s)

Practitioners and patients with pain

Industry/Entity Type

Business

Font styles to use
Sans Serif

Colors
3176b5
9bcb3b
ec1f27

Requirements
Must have
• The ability to communicate the message in the graphic
• Artistic flair
• Retain professionalism
Nice to have
• Unique creativity that distinguishes our product
• Matching with our logo (attached). Does not have to be the same colours or style/font but still should fit with the logo stylistically
Should not have
• A similar boring and flat feel as the existing graphics

```html
<!DOCTYPE html>
<html lang="en">
<head>
<meta charset="utf-8">
<title>Pacing: Overdo and Rest Cycle</title>
<link rel="stylesheet" href="https://fonts.googleapis.com/css2?family=Open+Sans:wght@400;600&display=swap">
<style>
  :root {
    --bg: #ffffff;
    --teal: #5dd6cf;
    --teal-deep: #1fb3aa;
    --teal-light: #9aeee8;
    --red: #e8174a;
    --red-deep: #c8232f;
    --red-bright: #ee4a3f;
  }
  html, body {
    margin: 0;
    padding: 0;
    width: 1200px;
    height: 1200px;
    overflow: hidden;
    background: var(--bg);
  }
  .pacing-chart {
    position: relative;
    width: 1200px;
    height: 1200px;
    font-family: "Open Sans", Arial, sans-serif;
  }
  .pacing-chart svg {
    position: absolute;
    inset: 0;
  }
  .axis-label {
    position: absolute;
    width: 130px;
    left: 61px;
    text-align: center;
    color: var(--teal);
    font-size: 21px;
    line-height: 25px;
    letter-spacing: 0.3px;
  }
  .axis-label--normal { top: 457px; }
  .axis-label--under { top: 679px; }
  .phase-label {
    position: absolute;
    width: 200px;
    text-align: center;
    transform: translateX(-50%);
  }
  .phase-label--overdo {
    top: 405px;
    color: var(--red);
    font-size: 16px;
  }
  .phase-label--rest {
    top: 752px;
    color: var(--teal);
    font-size: 20px;
  }
  .phase-marker {
    position: absolute;
    border-radius: 50%;
    transform: translate(-50%, -50%);
  }
  .phase-marker--overdo {
    width: 112px;
    height: 112px;
    background: radial-gradient(circle at 40% 40%, var(--red-bright), var(--red-deep));
  }
  .phase-marker--rest {
    width: 108px;
    height: 108px;
    background: radial-gradient(circle at 40% 40%, var(--teal-light), var(--teal-deep));
  }
</style>
</head>
<body>
<main class="pacing-chart">
  <svg width="1200" height="1200" viewBox="0 0 1200 1200" aria-hidden="true">
    <g class="axes" stroke="var(--teal)" stroke-width="6" stroke-linecap="round" fill="none">
      <path d="M198 388 L198 792 L1118 792"/>
    </g>
    <g class="axis-markers" stroke="var(--teal)" stroke-width="3.5" fill="#ffffff">
      <circle cx="198" cy="484" r="11"/>
      <circle cx="198" cy="703" r="11"/>
    </g>
    <polyline class="activity-line" fill="none" stroke="var(--teal)" stroke-width="3.5"
      points="234,701 337,701 386,556 436,701 598,701 648,556 698,701 860,701 909,556 958,701 1062,701"/>
  </svg>

  <div class="phase-marker phase-marker--rest" style="left:514px;top:690px" role="img" aria-label="Rest dial icon showing low activity"></div>
  <div class="phase-marker phase-marker--rest" style="left:776px;top:690px" role="img" aria-label="Rest dial icon showing low activity"></div>
  <div class="phase-marker phase-marker--overdo" style="left:384px;top:490px" role="img" aria-label="Overdo dial icon showing high activity"></div>
  <div class="phase-marker phase-marker--overdo" style="left:648px;top:490px" role="img" aria-label="Overdo dial icon showing high activity"></div>
  <div class="phase-marker phase-marker--overdo" style="left:908px;top:490px" role="img" aria-label="Overdo dial icon showing high activity"></div>

  <div class="axis-label axis-label--normal">NORMAL<br>ACTIVITY</div>
  <div class="axis-label axis-label--under">UNDER<br>ACTIVITY</div>

  <div class="phase-label phase-label--overdo" style="left:381px">OVERDO ACTIVITY</div>
  <div class="phase-label phase-label--overdo" style="left:647px">OVERDO ACTIVITY</div>
  <div class="phase-label phase-label--overdo" style="left:908px">OVERDO ACTIVITY</div>

  <div class="phase-label phase-label--rest" style="left:512px">REST</div>
  <div class="phase-label phase-label--rest" style="left:776px">REST</div>
</main>
</body>
</html>
```